依頼詳細
「日本労務審査支援連盟会」の概要・活動内容等を紹介するパンフレットの作成です。パンフレットとはいえ、A4裏表の簡易版でOKです(ページ数2ページ)。全体として、固い厳粛なイメージが出ればよいかと思います。記載する文章等は添付ファイルのとおりですので、配置や色、デザイン等の作成をお願いします。アレンジはお任せします。
記載項目
日本労務審査支援連盟会/ごあいさつ/協議会概要/活動内容(原則、添付ファイルの通り)
サイズ
A4
ページ数
両面
希望イメージ
シンプル 複雑
単色 カラフル
暗い 明るい
日常 高級
遊び心 厳粛
未来的 伝統的
女性的 男性的
希望する色
青系、茶系、グレー系、全体のバランスがよければ必ずしも上記に拘らないです。
納品ファイル
• PNG形式 (.png)
補足説明
協議会のWEBサイトは以下です。
http://romu-shien-renmei.com/
内容やイメージの参考にしてください。

やや硬いイメージを保ちつつ、シンプルで分かりやすいという点を判断基準として、選択いたしました。ありがとうございます。

この度は、多くのランサーの方からご提案いただき、大変ありがとうございます。改めて感謝申し上げます。
途中、修正依頼させていただいた方におかれましては、実際の選択ポイントからずれた内容で依頼してしまったこともあり、この点、お詫び申し上げます。(私以外の担当の意見も反映したことによるものです。何卒ご容赦ください。)
今後また案件が発生した際には、ご協力いただければ幸いです。
どうぞ宜しくお願いします。

```html
<!DOCTYPE html>
<html lang="ja">
<head>
<meta charset="utf-8">
<title>日本労務審査支援連盟会 活動内容・協議会概要</title>
<link href="https://fonts.googleapis.com/css2?family=Noto+Serif+JP:wght@400;600;700&family=Noto+Sans+JP:wght@500;700&display=swap" rel="stylesheet">
<style>
  :root {
    --wood: #5b3f2b;
    --wood-dark: #4a3222;
    --paper: #f1ebdc;
    --paper-light: #f7f2e6;
    --photo-a: #c9b99c;
    --photo-b: #e9dfcb;
    --heading: #4b2f1b;
    --rule: #6b4a30;
    --text: #3d3128;
    --badge: #6e4a2f;
    --cell-label: #cbc1b1;
    --cell-value: #ded7ca;
    --cell-line: #f6f2ea;
  }
  * { margin: 0; padding: 0; box-sizing: border-box; }
  html, body { width: 846px; height: 1200px; overflow: hidden; }
  body {
    position: relative;
    background: linear-gradient(180deg, var(--paper-light) 0%, var(--paper) 100%);
    font-family: "Noto Serif JP", serif;
    color: var(--text);
  }
  .wood-band { position: absolute; left: 0; width: 846px; background: linear-gradient(90deg, var(--wood-dark), var(--wood) 50%, var(--wood-dark)); }
  .wood-band.top { top: 0; height: 24px; }
  .wood-band.bottom { top: 1152px; height: 48px; }
  .hero-photo {
    position: absolute; left: 0; top: 24px; width: 846px; height: 520px;
    background:
      radial-gradient(ellipse at 70% 35%, rgba(140,118,88,0.55), rgba(140,118,88,0) 55%),
      linear-gradient(180deg, var(--photo-a) 0%, var(--photo-b) 70%, rgba(241,235,220,0) 100%);
  }
  .section-title {
    position: absolute; left: 133px; width: 584px; text-align: center;
    font-weight: 600; font-size: 30px; letter-spacing: 1px; color: var(--heading);
  }
  .title-rule { position: absolute; left: 133px; width: 584px; height: 14px; }
  .activity { position: absolute; left: 140px; width: 600px; }
  .activity-head { display: flex; align-items: center; height: 22px; font-family: "Noto Sans JP", sans-serif; font-weight: 700; font-size: 13.5px; color: #2e241c; }
  .badge { width: 23px; height: 21px; background: var(--badge); color: #fff; font-size: 13px; display: flex; align-items: center; justify-content: center; margin-right: 10px; font-weight: 500; }
  .activity-body { margin-top: 14px; font-size: 16px; line-height: 28px; color: #3a2f26; }
  .overview {
    position: absolute; left: 133px; top: 662px; width: 582px;
    border-collapse: collapse; font-size: 10.5px;
  }
  .overview th, .overview td { border-bottom: 2px solid var(--cell-line); }
  .overview th {
    width: 174px; background: var(--cell-label); border-right: 2px solid var(--cell-line);
    font-weight: 600; font-size: 14px; color: #2e241c; text-align: center;
  }
  .overview td { background: var(--cell-value); padding: 0 28px; line-height: 15px; color: #3a2f26; }
</style>
</head>
<body>
  <div class="wood-band top"></div>
  <div class="hero-photo" role="img" aria-label="明るいオフィスで握手を交わすスーツ姿のビジネスマン二人の写真"></div>

  <h2 class="section-title" style="top:114px;">活動内容</h2>
  <svg class="title-rule" style="top:150px;" viewBox="0 0 584 14">
    <line x1="0" y1="7" x2="584" y2="7" stroke="var(--rule)" stroke-width="1.5"/>
  </svg>

  <section class="activity" style="top:203px;">
    <div class="activity-head"><span class="badge">1</span>社会保険加入促進の啓蒙活動</div>
    <p class="activity-body">協議会所属の開業社会保険労務士によるセミナーの開催（自主開催）<br>業界団体様向けのセミナー・勉強会の開催<br>その他適正な情報の提供活動</p>
  </section>
  <section class="activity" style="top:352px;">
    <div class="activity-head"><span class="badge">2</span>社会保険調査リスク診断のご提供</div>
    <p class="activity-body">現状の社会保険上の問題点、保険料負担・法的リスクに関する診断サービス</p>
  </section>
  <section class="activity" style="top:443px;">
    <div class="activity-head"><span class="badge">3</span>社会保険調査対応＆コンサルティング</div>
    <p class="activity-body">国家資格取得者・社会保険調査対応の専門家として、的確な助言・指導の実施<br>各企業様の実情を踏まえた、コンサルティングサービスのご提供</p>
  </section>

  <h2 class="section-title" style="top:584px;">協議会概要</h2>
  <svg class="title-rule" style="top:623px;" viewBox="0 0 584 14">
    <line x1="0" y1="7" x2="584" y2="7" stroke="var(--rule)" stroke-width="1.5"/>
  </svg>

  <table class="overview">
    <tr style="height:34px;"><th>団体名</th><td>日本労務審査支援連盟会</td></tr>
    <tr style="height:85px;"><th>趣旨</th><td>社会保険 ( 厚生年金保険・健康保険・介護保険・雇用保険・労災保険 ) の適正な加入を促進及び加入支援をする目的として、会社保険の専門知識を有する国家資格「社会保険労務士」の全国の有志により設立された任意団体</td></tr>
    <tr style="height:35px;"><th>代表</th><td>柏木 正人 ( 社会保険労務士 ) 株式会社労務総研　代表取締役</td></tr>
    <tr style="height:34px;"><th>副代表</th><td>高峰直樹 ( 社会保険労務士 ) 労務監査対応協議会　代表</td></tr>
    <tr style="height:34px;"><th>特別アドバイザー</th><td>森田康弘 ( 社会保険労務士 ) 元年金事務所職員</td></tr>
    <tr style="height:34px;"><th>設立</th><td>2015 年</td></tr>
    <tr style="height:36px;"><th>所属社会保険労務士</th><td>40 名 (2015 年　　月現在 )</td></tr>
    <tr style="height:85px;"><th>事務局</th><td>〒100-0000 東京都千代田区丸の内 9-9-9 3F<br>東都人事労務ネットワーク<br>株式会社ワークブリッジ総研<br>代表取締役　高峰直樹 ( 社会保険労務士 )</td></tr>
    <tr style="height:34px;"><th>TEL</th><td>03-0000-1234(10:00～17:00)</td></tr>
    <tr style="height:34px;"><th>FAX</th><td>03-0000-1235</td></tr>
  </table>

  <div class="wood-band bottom"></div>
</body>
</html>
```